Redesign our iOS App Design mockups

- Redesign our current Veltro App Mockup
- Keep the design simple so that programmers do not have to do too much extra work to make your design work.
- Look at the attached website screenshot for the overall look and feel, and color scheme
- Convert the attached vector logo to iOS Icon format.
- Deliver all graphics in the density required for Veltro QL Prime.
- I have attached the current iOS mockup in a .ZIP file but you can view it here as well: https://boards.mockvault.net/share/QWTRPL8HNB2

Target Market(s)

Mostly Male Internet Consumers between the ages of 20 and 35

Industry/Entity Type

Internet

Colors

Designer to choose colors to be used in the design.

Requirements
Must have
• - Deliver all graphics in the density required for Veltro QL Prime
• - Should also look good on Tabrix and Tabrix pro
• - Design type should be “FLAT.”
• - Spell out fonts used in the design and where they are used. Also, include font sizes.
• - Please use ALL the elements in each page and use all placements and text EXACTLY. Please do not improvise with text or components.
• I have designed the mockup exactly the way I like it. I just want it to made to look better.
Should not have

```html
<!DOCTYPE html>
<html lang="en">
<head>
<meta charset="UTF-8">
<title>Forget Password</title>
<link href="https://fonts.googleapis.com/css2?family=Roboto:wght@400;500;700&display=swap" rel="stylesheet">
<style>
  :root {
    --brand: #f25f4e;
    --white: #ffffff;
    --ink: #222222;
    --body-ink: #333333;
    --muted: #777777;
    --footer-ink: #555555;
    --panel-bg: #f0f0f0;
    --panel-line: #c9c9c9;
    --input-line: #9a9a9a;
    --footer-bg: #f8f8f8;
    --footer-line: #e2e2e2;
  }
  html, body {
    margin: 0;
    padding: 0;
    width: 1200px;
    height: 2598px;
    overflow: hidden;
    background: var(--white);
  }
  .canvas {
    position: relative;
    width: 1200px;
    height: 2598px;
    overflow: hidden;
  }
  .screen {
    position: absolute;
    left: 0;
    top: 0;
    width: 375px;
    height: 812px;
    transform: scale(3.2);
    transform-origin: 0 0;
    font-family: "Roboto", Arial, sans-serif;
    background: var(--white);
    color: var(--ink);
  }
  .app-header {
    position: absolute;
    left: 0; top: 0;
    width: 375px; height: 88px;
    background: var(--brand);
  }
  .back-button {
    position: absolute;
    left: 12px; top: 40px;
    width: 20px; height: 24px;
  }
  .screen-title {
    position: absolute;
    left: 0; right: 0; top: 40px;
    margin: 0;
    text-align: center;
    font-size: 20px;
    font-weight: 400;
    line-height: 24px;
    color: var(--white);
  }
  .help-panel {
    position: absolute;
    left: 27px; top: 122px;
    width: 319px; height: 156px;
    background: var(--panel-bg);
    border: 1px solid var(--panel-line);
    border-radius: 4px;
    box-sizing: border-box;
  }
  .help-title {
    margin: 0;
    padding: 6px 14px 0;
    height: 38px;
    box-sizing: border-box;
    font-size: 18.5px;
    font-weight: 500;
    line-height: 26px;
    color: var(--ink);
    border-bottom: 1px solid var(--panel-line);
  }
  .help-text {
    margin: 0;
    padding: 6px 14px 0;
    font-size: 13px;
    line-height: 21px;
    color: var(--body-ink);
  }
  .field-label {
    position: absolute;
    left: 27px; top: 323px;
    font-size: 15px;
    font-weight: 700;
    line-height: 20px;
    color: var(--ink);
  }
  .email-input {
    position: absolute;
    left: 27px; top: 353px;
    width: 321px; height: 38px;
    box-sizing: border-box;
    border: 1px solid var(--input-line);
    border-radius: 19px;
    padding-left: 19px;
    font-size: 13.5px;
    line-height: 36px;
    color: var(--muted);
  }
  .primary-button {
    position: absolute;
    left: 27px; top: 412px;
    width: 162px; height: 38px;
    border-radius: 19px;
    background: var(--brand);
    color: var(--white);
    font-size: 15px;
    font-weight: 700;
    line-height: 38px;
    text-align: center;
  }
  .app-footer {
    position: absolute;
    left: 0; top: 692px;
    width: 375px; height: 120px;
    background: var(--footer-bg);
    border-top: 1px solid var(--footer-line);
    box-sizing: border-box;
  }
  .footer-prompt {
    position: absolute;
    left: 36px; top: 51px;
    font-size: 13px;
    line-height: 16px;
    color: var(--footer-ink);
  }
  .signup-button {
    position: absolute;
    left: 227px; top: 45px;
    width: 110px; height: 29px;
    border-radius: 15px;
    background: var(--brand);
    color: var(--white);
    font-size: 15px;
    font-weight: 700;
    line-height: 29px;
    text-align: center;
  }
</style>
</head>
<body>
<div class="canvas">
  <main class="screen">
    <header class="app-header">
      <svg class="back-button" viewBox="0 0 20 24" aria-label="Back">
        <polyline points="14,2 4,12 14,22" fill="none" stroke="#ffffff" stroke-width="2" stroke-linecap="round" stroke-linejoin="round"/>
      </svg>
      <h1 class="screen-title">Forget Password?</h1>
    </header>

    <section class="help-panel">
      <h2 class="help-title">Did You Forget your Password?</h2>
      <p class="help-text">If You have forgotten your password, enter the email addres associated with your account into the box below amd we will send you instructions on how to reset your password to your email account.</p>
    </section>

    <div class="field-label">Email Address:</div>
    <div class="email-input">Enter your email address</div>
    <div class="primary-button">Reset Password</div>

    <footer class="app-footer">
      <span class="footer-prompt">Don't have an Account yet?</span>
      <span class="signup-button">Sign Up</span>
    </footer>
  </main>
</div>
</body>
</html>
```